Business Card Design

We need a business card design for our new expansion based in Bloomfield Hills, Michigan. Our company is Quiet Harbor Institute & Wellness Center. Our Academy teaches individuals of all ages and professions to live from their soul. We teach intuitive development, meditation and mindfulness; shamanic healing. And ourr healing center provides holistic services. We offer certification programs that support the ethical practices of Intuitive professionals. Our team of Intuitive Practitioners includes: doctors, psychologists, chiropractor, soul retrievers, mediums, etc who all balance their knowledge with intuitive wisdom.

We want our symbol to be the Blue Morpho Buttefly and the colors on the card to complement it. We want to communicate inspiration, healing and empowerment. Thank you
Updates

Industry/Entity Type

Business

Contact Information for Business Card

Dana Orwick
Medium. Author. Soul Retriever.
Founder, Quiet Harbor

Quiet Harbor

19 North Cedar Mill Drive Suite 100
Fernwood Heights, MI 48517
248-603-7418

www.danaorwick.example

Requirements
Must have
• blue morpho butterfly

```html
<!DOCTYPE html>
<html lang="en">
<head>
<meta charset="utf-8">
<title>Quiet Harbor Institute &amp; Wellness Center – Business Card</title>
<link rel="stylesheet" href="https://fonts.googleapis.com/css2?family=Arimo:wght@400;700&display=swap">
<style>
  :root {
    --backdrop: #9a9a9a;
    --card-light: #9db9dd;
    --card-mid: #3f679f;
    --card-dark: #15285a;
    --navy: #101d4a;
    --accent-red: #f0453f;
    --text-white: #ffffff;
    --morpho-blue: #2e8fe0;
    --morpho-deep: #1c2f8a;
  }
  * { box-sizing: border-box; margin: 0; padding: 0; }
  html, body { width: 1200px; height: 800px; overflow: hidden; }
  body {
    background: var(--backdrop);
    font-family: "Arimo", Arial, sans-serif;
    position: relative;
  }
  .card {
    position: absolute;
    top: 252px;
    width: 525px;
    height: 300px;
    border-radius: 4px;
    overflow: hidden;
    box-shadow: 0 10px 24px rgba(0, 0, 0, 0.28);
  }
  .card--back {
    left: 50px;
    background: radial-gradient(ellipse 80% 90% at 35% 70%, var(--card-light) 0%, var(--card-mid) 48%, var(--card-dark) 100%);
  }
  .card--front {
    left: 625px;
    background: radial-gradient(ellipse 75% 85% at 50% 60%, var(--card-light) 0%, var(--card-mid) 50%, var(--card-dark) 100%);
  }

  /* Back: contact side */
  .brand-name {
    position: absolute;
    left: 30px;
    top: 24px;
    color: var(--navy);
    font-weight: 700;
    line-height: 1.05;
  }
  .brand-name__main { display: block; font-size: 36px; letter-spacing: 0.5px; }
  .brand-name__sub { display: block; font-size: 11px; letter-spacing: 3.2px; text-transform: uppercase; margin-top: 4px; }

  .contact {
    position: absolute;
    left: 30px;
    top: 106px;
    width: 250px;
  }
  .contact__name {
    color: var(--accent-red);
    font-weight: 700;
    font-size: 22px;
  }
  .contact__role-tag { font-size: 12px; font-weight: 400; }
  .contact__titles {
    color: var(--text-white);
    font-weight: 700;
    font-size: 11.5px;
    margin-top: 3px;
  }
  .contact__rule {
    border: 0;
    border-top: 2px dotted var(--accent-red);
    margin: 8px 0 10px;
    width: 240px;
  }
  .contact__list { list-style: none; }
  .contact__item {
    display: flex;
    align-items: flex-start;
    gap: 8px;
    color: var(--text-white);
    font-weight: 700;
    font-size: 11.5px;
    line-height: 1.35;
    margin-bottom: 7px;
  }
  .contact__icon { width: 12px; height: 12px; flex: none; margin-top: 2px; }

  .brand-dot {
    position: absolute;
    right: 70px;
    top: 120px;
    width: 130px;
    height: 130px;
    border-radius: 50%;
    background: var(--morpho-blue);
    box-shadow: inset 0 0 0 8px var(--morpho-deep);
  }

  /* Front: logo side */
  .front-name {
    position: absolute;
    left: 0;
    right: 0;
    top: 112px;
    text-align: center;
    color: var(--navy);
    font-weight: 700;
    line-height: 1.1;
  }
  .front-name__main { display: block; font-size: 40px; letter-spacing: 0.5px; }
  .front-name__sub { display: block; font-size: 12px; letter-spacing: 3.6px; text-transform: uppercase; margin-top: 6px; }
</style>
</head>
<body>

<section class="card card--back" aria-label="Business card, contact side">
  <h1 class="brand-name">
    <span class="brand-name__main">Quiet Harbor</span>
    <span class="brand-name__sub">Institute &amp; Wellness Center</span>
  </h1>

  <div class="contact">
    <p class="contact__name">Dana Orwick<span class="contact__role-tag">, founder</span></p>
    <p class="contact__titles">Medium, Author, Soul Retriever</p>
    <hr class="contact__rule">
    <ul class="contact__list">
      <li class="contact__item">
        <svg class="contact__icon" viewBox="0 0 12 12" aria-hidden="true"><path d="M1 3c0-1 1-2 2-2l1.5 2.5L3.5 5c.7 1.4 2 2.7 3.5 3.5l1.5-1L11 9c0 1-1 2-2 2C4.6 11 1 7.4 1 3z" fill="var(--accent-red)"/></svg>
        <span>248-603-7418</span>
      </li>
      <li class="contact__item">
        <svg class="contact__icon" viewBox="0 0 12 12" aria-hidden="true"><path d="M6 0.5C3.8 0.5 2.2 2.1 2.2 4.2 2.2 7 6 11.5 6 11.5S9.8 7 9.8 4.2C9.8 2.1 8.2 0.5 6 0.5zm0 5.2a1.5 1.5 0 1 1 0-3 1.5 1.5 0 0 1 0 3z" fill="var(--accent-red)"/></svg>
        <span>19 North Cedar Mill Drive Suite 100<br>Fernwood Heights, MI 48517</span>
      </li>
      <li class="contact__item">
        <svg class="contact__icon" viewBox="0 0 12 12" aria-hidden="true"><circle cx="6" cy="6" r="5" fill="none" stroke="var(--accent-red)" stroke-width="1.3"/><path d="M1 6h10M6 1c-2.5 3-2.5 7 0 10M6 1c2.5 3 2.5 7 0 10" fill="none" stroke="var(--accent-red)" stroke-width="1"/></svg>
        <span>www.danaorwick.example</span>
      </li>
    </ul>
  </div>

  <div class="brand-dot" aria-hidden="true"></div>
</section>

<section class="card card--front" aria-label="Business card, logo side">
  <h2 class="front-name">
    <span class="front-name__main">Quiet Harbor</span>
    <span class="front-name__sub">Institute &amp; Wellness Center</span>
  </h2>
</section>

</body>
</html>
```